Finance cashflow waterfall graphic

Recreate "Cashflow Waterfall Example 1" - waterfall term used to explain the different accounts and priority that need to be paid as part of a apartment building / project. Create simple, business professional graphic for real estate report. Check the inspiration image but change to dorm building, no people - potentially combine the two images... Ideally editable so I can change the names of the accounts / colors / etc.

```html
<!DOCTYPE html>
<html lang="en">
<head>
<meta charset="utf-8">
<title>Cashflow Waterfall</title>
<link rel="stylesheet" href="https://fonts.googleapis.com/css2?family=Roboto:wght@500;700;900&display=swap">
<style>
  :root {
    --stage: #3e3e3e;
    --frame: #1478b4;
    --panel-edge: #b3ddf2;
    --panel-core: #f4fbff;
    --ring: #6cc3e6;
    --ink: #0c1f3f;
    --watermark: rgba(80,170,225,0.26);
    --node: #1592d2;
    --node-total: #0f7cc0;
    --node-edge: #0f3567;
    --node-halo: #ffffff;
    --icon: #ffffff;
  }
  * { margin: 0; padding: 0; box-sizing: border-box; }
  html, body { width: 1200px; height: 948px; overflow: hidden; background: var(--stage); }
  .canvas { position: relative; width: 1200px; height: 948px; font-family: "Roboto", Arial, sans-serif; }
  .card-frame {
    position: absolute; left: 102px; top: 89px; width: 996px; height: 771px;
    background: var(--frame);
    box-shadow: 0 10px 30px rgba(0,0,0,0.45);
  }
  .card-panel {
    position: absolute; left: 122px; top: 104px; width: 957px; height: 740px; overflow: hidden;
    background: radial-gradient(ellipse 620px 480px at 494px 384px, var(--panel-core) 0%, var(--panel-edge) 100%);
  }
  .diagram { position: absolute; left: 0; top: 0; width: 1200px; height: 948px; }
  .label {
    position: absolute; color: var(--ink); font-weight: 500; font-size: 20px; line-height: 24px; white-space: nowrap;
  }
  .label--center { transform: translateX(-50%); text-align: center; }
  .label--right { transform: translateX(-100%); text-align: right; }
  .label--mid { margin-top: -12px; }
  .label--total { font-weight: 700; font-size: 29px; line-height: 34px; }
</style>
</head>
<body>
<div class="canvas">
  <div class="card-frame"></div>
  <div class="card-panel"></div>

  <svg class="diagram" viewBox="0 0 1200 948" xmlns="http://www.w3.org/2000/svg">
    <defs>
      <clipPath id="panel-clip"><rect x="122" y="104" width="957" height="740"/></clipPath>

      <symbol id="node" viewBox="-32 -32 64 64">
        <circle r="29" fill="var(--node)" stroke="var(--node-halo)" stroke-width="4"/>
        <circle r="26.5" fill="none" stroke="var(--node-edge)" stroke-width="1.5"/>
      </symbol>
      <symbol id="node-total" viewBox="-32 -32 64 64">
        <circle r="29.5" fill="var(--node-total)" stroke="var(--node-halo)" stroke-width="2.5"/>
        <circle r="28" fill="none" stroke="var(--node-edge)" stroke-width="0.8"/>
      </symbol>

      <symbol id="icon-bank" viewBox="-30 -30 60 60">
        <g fill="var(--icon)">
          <path d="M-15 -6 L0 -15 L15 -6 Z"/>
          <rect x="-13" y="-4" width="4" height="13"/><rect x="-6" y="-4" width="4" height="13"/>
          <rect x="2" y="-4" width="4" height="13"/><rect x="9" y="-4" width="4" height="13"/>
          <rect x="-15" y="10" width="30" height="4"/>
        </g>
      </symbol>
      <symbol id="icon-briefcase" viewBox="-30 -30 60 60">
        <g fill="var(--icon)">
          <path d="M-6 -12 h12 v5 h-3 v-2 h-6 v2 h-3 Z"/>
          <rect x="-15" y="-7" width="30" height="8" rx="1.5"/>
          <rect x="-15" y="3" width="30" height="10" rx="1.5"/>
          <rect x="-3" y="-1" width="6" height="5" fill="var(--node)"/>
        </g>
      </symbol>
      <symbol id="icon-cash" viewBox="-30 -30 60 60">
        <g fill="none" stroke="var(--icon)" stroke-width="2.5" stroke-linecap="round">
          <path d="M-11 -12 L11 -16 M-9 -9 L13 -13"/>
          <rect x="-16" y="-6" width="32" height="16" rx="1.5"/>
          <circle cx="0" cy="2" r="3.5" fill="var(--icon)"/>
        </g>
      </symbol>
      <symbol id="icon-hourglass" viewBox="-30 -30 60 60">
        <g fill="var(--icon)">
          <rect x="-11" y="-15" width="22" height="4" rx="1"/>
          <rect x="-11" y="11" width="22" height="4" rx="1"/>
          <path d="M-8 -11 H8 L2 0 L8 11 H-8 L-2 0 Z" fill="none" stroke="var(--icon)" stroke-width="2.5" stroke-linejoin="round"/>
          <path d="M-6 11 L0 4 L6 11 Z"/>
        </g>
      </symbol>
      <symbol id="icon-laptop" viewBox="-30 -30 60 60">
        <g fill="none" stroke="var(--icon)" stroke-width="2.5" stroke-linecap="round">
          <rect x="-11" y="-10" width="22" height="14" rx="1"/>
          <path d="M-16 9 H16"/>
        </g>
      </symbol>
      <symbol id="icon-chart" viewBox="-30 -30 60 60">
        <g fill="var(--icon)">
          <path d="M-16 -17 V15 H17" fill="none" stroke="var(--icon)" stroke-width="2.5"/>
          <rect x="-11" y="4" width="6" height="8"/>
          <rect x="-2" y="-3" width="6" height="15"/>
          <rect x="7" y="-14" width="6" height="26"/>
          <path d="M-11 -1 L0 -12" fill="none" stroke="var(--icon)" stroke-width="2.5" stroke-linecap="round"/>
          <path d="M-4 -14 L3 -15 L2 -8 Z"/>
        </g>
      </symbol>
      <symbol id="icon-reserves" viewBox="-30 -30 60 60">
        <g fill="var(--icon)">
          <ellipse cx="0" cy="10" rx="12" ry="4"/>
          <rect x="-12" y="2" width="24" height="8"/>
          <ellipse cx="0" cy="2" rx="12" ry="4" stroke="var(--node)" stroke-width="1.5"/>
          <rect x="-12" y="-7" width="24" height="9"/>
          <ellipse cx="0" cy="-7" rx="12" ry="4" stroke="var(--node)" stroke-width="1.5"/>
        </g>
      </symbol>
      <symbol id="icon-split" viewBox="-30 -30 60 60">
        <g fill="var(--icon)">
          <path d="M2 1 V-15 A16 16 0 1 1 -13 10 Z"/>
          <path d="M-2 -2 L-15 5 A16 16 0 0 1 -2 -17 Z" opacity="0.75"/>
        </g>
      </symbol>
    </defs>

    <g clip-path="url(#panel-clip)">
      <text class="watermark" x="139" y="835" textLength="924" lengthAdjust="spacingAndGlyphs"
            font-family="Roboto, Arial, sans-serif" font-weight="900" font-size="214" fill="var(--watermark)">REVENUE</text>
    </g>

    <path class="flow-ring" d="M378 438 A235 235 0 1 1 683 670" fill="none" stroke="var(--ring)" stroke-width="5"/>

    <g class="nodes">
      <use href="#node" x="561" y="182" width="64" height="64"/><use href="#icon-bank" x="563" y="184" width="60" height="60"/>
      <use href="#node" x="744" y="234" width="64" height="64"/><use href="#icon-briefcase" x="746" y="236" width="60" height="60"/>
      <use href="#node" x="389" y="282" width="64" height="64"/><use href="#icon-cash" x="391" y="284" width="60" height="60"/>
      <use href="#node" x="816" y="393" width="64" height="64"/><use href="#icon-hourglass" x="818" y="395" width="60" height="60"/>
      <use href="#node" x="773" y="562" width="64" height="64"/><use href="#icon-laptop" x="775" y="564" width="60" height="60"/>
      <use href="#node" x="345" y="445" width="64" height="64"/><use href="#icon-reserves" x="347" y="447" width="60" height="60"/>
      <use href="#node" x="412" y="465" width="42" height="42"/><use href="#icon-split" x="414" y="467" width="38" height="38"/>
      <use href="#node-total" x="546" y="636" width="140" height="140"/><use href="#icon-chart" x="572" y="662" width="88" height="88"/>
    </g>
  </svg>

  <div class="label label--center" style="left:616px; top:131px;">Recapitalization Account</div>
  <div class="label label--mid" style="left:823px; top:266px;">Asset Management Fees</div>
  <div class="label label--right label--mid" style="left:373px; top:311px;">Incentive Fees</div>
  <div class="label label--mid" style="left:892px; top:426px;">Debt Payment</div>
  <div class="label label--mid" style="left:849px; top:602px;">Operating Expenses</div>
  <div class="label label--right" style="left:330px; top:444px;">Sustainment<br>Reserves / Member<br>Distribution (60%)</div>
  <div class="label" style="left:470px; top:444px;">Private Returns /<br>Managing Member<br>Distribution (40%)</div>
  <div class="label label--center label--total" style="left:616px; top:789px;">Revenue</div>
</div>
</body>
</html>
```